4 panel brochure for funding campaign

-This will be a four panel folded brochure for a church expansion project. The flat size of the brochure will be 15.25" x 9.25" The brochure will fold in half and then "short" fold to 4" (this will create an extended tab on the right hand side of the brochure). The 4th panel will be a perforated donation reply form.
-Prints 4/4 with bleeds.
-There will need to be a floor plan included (for now we can provide a jpg, but are working on sending you a vector).
-There will be 5 major sections to the brochure:
1. Reasons for the Project
2. Floorplan
3. Naming Opportunities
4. How you can help
5 Pledge Card
-All copy will be provided.

Target Market(s)

Donors

Industry/Entity Type

Church

Requirements
Must have
• Colorful - but not edgy.
The floorplan must be color coded to match the NAMING opportunities.

```html
<!DOCTYPE html>
<html lang="en">
<head>
<meta charset="utf-8">
<title>Continuing the Vision – Campaign Brochure</title>
<link rel="stylesheet" href="https://fonts.googleapis.com/css2?family=Josefin+Slab:wght@300;400;600&family=Tinos:ital,wght@0,400;0,700;1,400&display=swap">
<style>
  :root {
    --page: #ecebe7;
    --paper: #ffffff;
    --sky: #3fb3e3;
    --sky-tint: #e2f2fa;
    --olive: #8c9a3c;
    --olive-tint: #cfd09d;
    --cream: #f4f0e1;
    --salmon: #d8694a;
    --salmon-tint: #e89a82;
    --leaf: #9cbf5d;
    --ink: #2f2f2f;
    --grey: #8d8d8d;
    --charcoal: #3a3a3a;
    --display: "Josefin Slab", serif;
    --body: "Tinos", serif;
  }
  * { box-sizing: border-box; margin: 0; padding: 0; }
  html, body { width: 1200px; height: 1200px; overflow: hidden; background: var(--page); }
  body { position: relative; font-family: var(--body); color: var(--ink); }

  .spread {
    position: absolute; left: 150px; width: 900px; height: 546px;
    background: var(--paper); display: flex;
    box-shadow: 0 1px 4px rgba(0,0,0,.12);
  }
  .spread--outside { top: 36px; }
  .spread--inside { top: 618px; }
  .panel { position: relative; height: 100%; overflow: hidden; }

  /* Pledge card */
  .pledge { width: 234px; background: var(--sky-tint); border-right: 1px dashed #9fcbe0; padding: 78px 18px 0 18px; font-size: 8.6px; line-height: 1.45; }
  .pledge__title { position: absolute; top: 18px; left: 40px; right: 0; height: 40px; background: var(--sky); color: #fff; font-family: var(--display); font-weight: 400; font-size: 23px; line-height: 42px; padding-left: 18px; }
  .pledge p { margin-bottom: 9px; }
  .field { display: flex; }
  .field span.line { flex: 1; border-bottom: 1px solid var(--ink); margin: 0 2px 3px 2px; }

  /* Cover */
  .cover { width: 212px; text-align: center; }
  .cover__title { font-family: var(--display); font-weight: 300; color: var(--grey); font-size: 33px; line-height: 1; margin-top: 26px; }
  .cover__title small { display: block; font-size: 11px; margin: 2px 0 -2px 60px; }
  .cover__title .big { font-size: 46px; }
  .cover__photo { position: absolute; left: 0; right: 0; top: 220px; bottom: 0; background: linear-gradient(180deg, #c9d1d6 0%, #aeb7a7 35%, #6f7a55 55%, #5f8a3c 75%, #7fa64b 100%); }

  /* Reasons */
  .reasons { width: 212px; background: var(--olive-tint); }
  .reasons__title { margin: 18px 0 0 0; height: 64px; background: var(--olive); color: #fff; font-family: var(--display); font-weight: 400; font-size: 31px; line-height: 1; padding: 10px 0 0 20px; }
  .reasons__title small { font-size: 11px; margin-left: 16px; }
  .reasons__title .sub { font-size: 26px; }
  .reasons ul { list-style: none; text-align: center; padding: 26px 16px 0; font-size: 9.2px; line-height: 1.35; }
  .reasons li { margin-bottom: 11px; }
  .reasons li::before { content: "• "; }

  /* How you can help */
  .help { width: 242px; padding: 0 30px 0 18px; font-size: 8.8px; line-height: 1.45; }
  .help::after { content: ""; position: absolute; top: 0; right: 0; width: 12px; height: 100%; background: var(--olive); }
  .help__title { font-family: var(--display); font-weight: 300; color: var(--grey); font-size: 30px; line-height: .95; margin: 18px 0 18px 40px; }
  .help__title .you { color: var(--olive); font-size: 58px; font-weight: 400; }
  .help__title .rest { font-size: 26px; }
  .help p { margin-bottom: 12px; }
  .mission__title { font-family: var(--display); color: var(--olive); font-size: 17px; line-height: 1; text-align: right; margin: 22px 0 14px; }
  .mission__title small { display: block; font-size: 14px; }

  /* Inside: floorplan */
  .floorplan { width: 560px; }
  .floorplan__tag { position: absolute; top: 22px; left: 22px; width: 150px; height: 52px; background: var(--charcoal); color: #e4e4e4; font-family: var(--display); font-weight: 300; font-size: 21px; line-height: 1; padding: 8px 0 0 12px; }
  .floorplan__tag small { font-size: 9px; margin-left: 40px; }
  .floorplan__drawing { position: absolute; left: 22px; right: 18px; top: 90px; bottom: 22px; background: linear-gradient(135deg, #f1f1ef, #e3e3df); }

  /* Naming options */
  .naming { width: 340px; background: var(--cream); padding: 26px 26px 0 34px; }
  .naming::before { content: ""; position: absolute; left: 22px; top: 0; bottom: 0; width: 1px; background: var(--salmon); }
  .naming__title { font-family: var(--display); font-weight: 300; color: var(--salmon); font-size: 46px; line-height: .9; }
  .naming__title small { display: block; font-size: 22px; margin-left: 30px; }
  .options { list-style: none; margin-top: 18px; font-size: 9.4px; line-height: 1.35; }
  .options li { padding: 3px 8px; margin-bottom: 5px; }
  .options .row { display: flex; }
  .options .row span.dots { flex: 1; border-bottom: 1px dotted var(--ink); margin: 0 3px 3px; }
  .options .sub { padding-left: 12px; }
  .options .highlight--leaf { background: var(--leaf); }
  .options .highlight--salmon { background: var(--salmon-tint); }
</style>
</head>
<body>

<section class="spread spread--outside">
  <div class="panel pledge">
    <h2 class="pledge__title">Pledge Card</h2>
    <p>Church of the Still Waters<br>Continuing the Vision Campaign</p>
    <div class="field">Donor Name<span class="line"></span></div>
    <div class="field">Address<span class="line"></span></div>
    <div class="field">City<span class="line"></span>State<span class="line"></span>Zip<span class="line"></span></div>
    <div class="field">Best contact phone number<span class="line"></span></div>
    <div class="field">Total pledge amount $<span class="line"></span></div>
    <div class="field">Paid with pledge $<span class="line"></span>Balance $<span class="line"></span></div>
    <p style="margin-top:9px">Payment schedule<br>(A payment schedule of no more than three years is preferred, if possible. Thank you.)</p>
    <div class="field"><span class="line"></span></div>
    <p style="margin-top:9px">Naming Gift<br>(Name of area/item you wish to sponsor)</p>
    <div class="field"><span class="line"></span></div>
    <p style="margin-top:9px">If gift is given in honor or memory of another, please complete:</p>
    <div class="field">In honor of<span class="line"></span></div>
    <div class="field">In memory of<span class="line"></span></div>
    <div class="field" style="margin-top:8px">Signature<span class="line"></span></div>
    <div class="field" style="margin-bottom:9px">Date<span class="line"></span></div>
    <p>Please make your check payable to Church of the Still Waters Capital Campaign. All gifts are tax deductible to the fullest extent of the law.</p>
    <p>Church of the Still Waters<br>1208 Meadow Lane<br>Fairview, PA 17000</p>
  </div>

  <div class="panel cover">
    <h1 class="cover__title">Continuing<small>the</small><span class="big">Vision</span></h1>
    <div class="cover__photo" role="img" aria-label="Photograph of the church building with its steeple, trees and green lawn"></div>
  </div>

  <div class="panel reasons">
    <h2 class="reasons__title">Reasons<br><small>for the</small> <span class="sub">Project</span></h2>
    <ul>
      <li>Lack of proper waiting area</li>
      <li>Inadequate number of private offices</li>
      <li>Lack of general storage</li>
      <li>Lack of work space for staff</li>
      <li>Lack of adequate private space for personal discussion</li>
      <li>Lack of conference room for advisory council meetings</li>
      <li>Lack of space for today’s technology and office equipment</li>
      <li>Lack of space for archival materials</li>
      <li>Overall “tiredness” of aging furnishings and flooring</li>
    </ul>
  </div>

  <div class="panel help">
    <h2 class="help__title">How<br><span class="you">you</span> <span class="rest">can help</span></h2>
    <p>Please consider a pledge to this campaign. Gifts of all sizes create a powerful, cumulative effect. Pledges of up to three years are preferred.</p>
    <p>Gifts of $5,000 and more will be recognized on a Donor Recognition Plaque in the new parish Waiting Room. In addition, parishioners who sponsor an item will receive special recognition on a plaque in their sponsoring area.</p>
    <h3 class="mission__title">Still Waters’<small>Mission Statement</small></h3>
    <p>To deepen our personal relationship with God.</p>
    <p>To foster a faith-filled community.</p>
    <p>To provide opportunities to grow in the Catholic faith.</p>
    <p>To share the good news of Jesus Christ.</p>
    <p>To promote Christian service to all people.</p>
  </div>
</section>

<section class="spread spread--inside">
  <div class="panel floorplan">
    <div class="floorplan__tag">Continuing<br><small>the</small> Vision</div>
    <div class="floorplan__drawing" role="img" aria-label="Architectural floor plan of the parish offices and church, with the sponsored rooms colour coded in salmon and green"></div>
  </div>

  <div class="panel naming">
    <h2 class="naming__title">Floorplan<small>naming options</small></h2>
    <ul class="options">
      <li class="highlight--leaf"><div class="row">Conference Room<span class="dots"></span>$25,000</div><div class="row sub">Furnishings<span class="dots"></span>$10,000</div></li>
      <li class="highlight--salmon"><div class="row">Pastor’s Office<span class="dots"></span>$30,000</div><div class="row sub">Furnishings<span class="dots"></span>$10,000</div></li>
      <li><div class="row">Parish Manager’s Office<span class="dots"></span>$30,000</div><div class="row sub">Furnishings<span class="dots"></span>$10,000</div></li>
      <li><div class="row">Parochial Vicar’s Office<span class="dots"></span>$30,000</div><div class="row sub">Furnishings<span class="dots"></span>$5,000</div></li>
      <li><div class="row">Archivist Room<span class="dots"></span>$30,000</div><div class="row sub">Furnishings<span class="dots"></span>$5,000</div></li>
      <li><div class="row">Caring Team Ministry Room<span class="dots"></span>$30,000</div><div class="row sub">Furnishings<span class="dots"></span>$5,000</div></li>
      <li><div class="row">Waiting Room<span class="dots"></span>$30,000</div><div class="row sub">Furnishings<span class="dots"></span>$20,000</div></li>
      <li><div class="row">General Office area<span class="dots"></span></div><div class="row sub">Administrative work stations (3)<span class="dots"></span>$10,000 each</div></li>
      <li><div class="row">Covered Entry<span class="dots"></span>$20,000</div></li>
      <li><div class="row">Break Room/Counting Room<span class="dots"></span>$15,000</div><div class="row sub">Furnishings &amp; appliances<span class="dots"></span>$8,000</div></li>
      <li><div class="row">Copy/Work Area<span class="dots"></span>$10,000</div></li>
      <li><div class="row">Technology Room<span class="dots"></span>$10,000</div></li>
      <li><div class="row">Landscaping<span class="dots"></span>$10,000</div></li>
      <li><div class="row">Storage Rooms (3)<span class="dots"></span>$2,000 each</div></li>
    </ul>
  </div>
</section>

</body>
</html>
```